Cover design for new academic journal on deconstruction and psychoanalysis

We need a cover for a new academic journal on deconstruction and psychoanalysis. The name of the journal is "The Liminal Remainder: A Journal of Deconstruction and Psychoanalysis" (LR) and it is published by the Calloway Ridge University Press(CRP).

Here is a description of the journal on the CRP website:

http://www.callowayridgepress.example.edu/product/The-Liminal-Remainder,482917.aspx

We are looking for a design that is more abstract and does not have icons or photographs of people, especially not photos of Valmont or Kessler. The design should be contemporary with clean lines and simple fonts. Again, it should be abstract, with no icons or iconography.

The cover should simply have the full name of the journal and then "Volume 1, Issue 1, 2014" on the cover and "Vol. 1, No. 1, 2014" on the spine.

Attached you can see some ideas that we rejected from CRP. It is important that you understand that these designs were rejected and are just being offered as examples of what the cover will look like in general, as a template of sorts.

The cover should have a bold abstract design, with a space for the title and "Volume 1, Issue 1, 2014."

Something bold and contemporary.

Academics, scholars and psychoanalysts.

University

Sans Serif

• Must be abstract, bold, have color, and must be contemporary.
• No icons, no photographs of Valmont, Kessler, or anyone.

```html
<!DOCTYPE html>
<html lang="en">
<head>
<meta charset="utf-8">
<title>The Liminal Remainder — Volume 1, Issue 1, 2014</title>
<link href="https://fonts.googleapis.com/css2?family=Bebas+Neue&family=Crimson+Text:ital@0;1&display=swap" rel="stylesheet">
<style>
  :root {
    --paper: #ffffff;
    --frame: #111111;
    --sky-top: #5f93cf;
    --sky-horizon: #b7d0ea;
    --sea-surface: #3a5b82;
    --sea-mid: #1f3c63;
    --sea-deep: #122747;
    --ice: #dfe9f2;
    --ink-light: #ffffff;
  }
  html, body {
    margin: 0;
    padding: 0;
    width: 875px;
    height: 1200px;
    overflow: hidden;
    background: var(--paper);
  }
  .cover {
    position: relative;
    width: 875px;
    height: 1200px;
    background: var(--paper);
    box-sizing: border-box;
  }
  .cover-frame {
    position: absolute;
    left: 4px; top: 4px; right: 4px; bottom: 4px;
    border: 2px solid var(--frame);
  }
  .cover-art {
    position: absolute;
    left: 30px; top: 31px;
    width: 815px; height: 1135px;
    background: linear-gradient(to bottom,
      var(--sky-top) 0%,
      var(--sky-horizon) 29%,
      var(--sea-surface) 29%,
      var(--sea-mid) 55%,
      var(--sea-deep) 100%);
  }
  .cover-art .ice-mass {
    position: absolute;
    left: 105px; top: 60px;
    width: 600px; height: 880px;
    background: radial-gradient(ellipse at 50% 30%, rgba(223,233,242,0.55) 0%, rgba(223,233,242,0.18) 45%, rgba(223,233,242,0) 70%);
  }
  .issue-line {
    position: absolute;
    top: 72px; left: 0; right: 0;
    text-align: center;
    font-family: "Crimson Text", Georgia, serif;
    font-size: 22px;
    color: var(--ink-light);
    margin: 0;
  }
  .journal-title {
    position: absolute;
    top: 382px; left: 0; right: 0;
    margin: 0;
    text-align: center;
    font-family: "Bebas Neue", "Arial Narrow", sans-serif;
    font-weight: 400;
    font-size: 84px;
    line-height: 74px;
    letter-spacing: 1px;
    color: var(--ink-light);
  }
  .journal-title span { display: block; }
  .journal-subtitle {
    position: absolute;
    top: 610px; left: 0; right: 0;
    margin: 0;
    text-align: center;
    font-family: "Crimson Text", Georgia, serif;
    font-style: italic;
    font-size: 30px;
    line-height: 38px;
    color: var(--ink-light);
  }
  .journal-subtitle span { display: block; }
  .publisher {
    position: absolute;
    top: 1055px; left: 0; right: 0;
    margin: 0;
    text-align: center;
    font-family: "Crimson Text", Georgia, serif;
    font-variant: small-caps;
    font-size: 22px;
    letter-spacing: 1px;
    color: var(--ink-light);
  }
</style>
</head>
<body>
  <main class="cover">
    <div class="cover-frame"></div>
    <div class="cover-art" role="img" aria-label="Photograph of an iceberg rising from a calm blue sea, its larger mass visible beneath the waterline">
      <div class="ice-mass"></div>
    </div>
    <p class="issue-line">Volume 1, Issue 1, 2014</p>
    <h1 class="journal-title">
      <span>The</span>
      <span>Liminal</span>
      <span>Remainder</span>
    </h1>
    <p class="journal-subtitle">
      <span>A Journal of</span>
      <span>Deconstruction and</span>
      <span>Psychoanalysis</span>
    </p>
    <p class="publisher">Calloway Ridge University Press</p>
  </main>
</body>
</html>
```